Brightwell Recovery Email Marketing Design

Dear Designer,
We're in need of an email background template for our company, Brightwell Recovery, that reflects our commitment to building lasting relationships with our clients and providing top-quality restoration and cleaning services.
We'd like the template to incorporate our brand colors, which are #F2F2F3, #005EA5, #468ECC, and #000000, and to feature images related to our services, such as water restoration, emergency flood response, mold remediation, trauma scene clean-up, fire restoration, carpet cleaning, and more. Our logo and tagline, "Calm Returns", should be prominently displayed in a unique and visually appealing way, along with our website address, www.brightwellrecovery.example.
The email should be professional and positive, highlighting the camaraderie and teamwork among our employees. We want to thank our clients for their business, offer a special discount, and promote our services. The final design should be visually stunning and memorable, with a clear call-to-action to encourage clients to take advantage of the discount.
We'd like the final design in JPG or PNG format, with a resolution of at least 720x720 pixels.
Thank you for considering this project. We're excited to see what you come up with!
Best regards,
Tavin

```html
<!DOCTYPE html>
<html lang="en">
<head>
<meta charset="utf-8">
<title>Brightwell Recovery – Calm Returns</title>
<link rel="stylesheet" href="https://fonts.googleapis.com/css2?family=Montserrat:wght@600;700&family=Playfair+Display:wght@600;700&display=swap">
<style>
  :root {
    --brand-blue: #0a57b0;
    --brand-blue-deep: #0b4ea3;
    --brand-blue-soft: #468ecc;
    --paper: #f2f2f3;
    --white: #ffffff;
    --ink: #000000;
    --tick: #7fa8da;
  }
  * { margin: 0; padding: 0; box-sizing: border-box; }
  html, body { width: 1200px; height: 1200px; overflow: hidden; }
  body { background: var(--brand-blue); font-family: "Montserrat", Arial, sans-serif; }

  .email-card {
    position: relative;
    width: 1200px;
    height: 1200px;
    overflow: hidden;
    background: radial-gradient(circle at 30% 70%, #0f5fbb 0%, var(--brand-blue) 45%, var(--brand-blue-deep) 100%);
    color: var(--white);
  }

  .brand-name {
    position: absolute;
    left: 59px;
    top: 58px;
    font-family: "Playfair Display", Georgia, serif;
    font-weight: 700;
    font-size: 34px;
    letter-spacing: 0.5px;
    color: var(--white);
  }

  .headline {
    position: absolute;
    left: 57px;
    top: 160px;
    font-family: "Playfair Display", Georgia, serif;
    font-weight: 700;
    font-size: 84px;
    line-height: 88px;
    text-transform: uppercase;
    letter-spacing: 0.5px;
  }

  .rule {
    position: absolute;
    left: 59px;
    width: 218px;
    height: 6px;
    background: var(--brand-blue-soft);
    opacity: 0.85;
  }
  .rule--headline { top: 346px; }
  .rule--services { top: 626px; }

  .intro {
    position: absolute;
    left: 59px;
    top: 385px;
    width: 470px;
    font-weight: 700;
    font-size: 23px;
    line-height: 29.5px;
  }

  .section-title {
    position: absolute;
    left: 59px;
    top: 560px;
    font-family: "Playfair Display", Georgia, serif;
    font-weight: 600;
    font-size: 37px;
  }

  .service-list { list-style: none; position: absolute; left: 59px; top: 658px; }
  .service-list li {
    display: flex;
    align-items: center;
    height: 63.5px;
    font-weight: 700;
    font-size: 23px;
  }
  .service-list svg { width: 31px; height: 31px; margin-right: 27px; flex: none; }

  .cta-button {
    position: absolute;
    left: 59px;
    top: 936px;
    width: 250px;
    height: 72px;
    border-radius: 36px;
    background: var(--white);
    color: var(--brand-blue);
    font-weight: 700;
    font-size: 28px;
    display: flex;
    align-items: center;
    justify-content: center;
    letter-spacing: 0.5px;
  }

  .web-band {
    position: absolute;
    left: 0;
    top: 1049px;
    width: 1000px;
    height: 97px;
    background: var(--paper);
    display: flex;
    align-items: center;
    padding-left: 58px;
    color: var(--brand-blue);
    font-weight: 700;
    font-size: 23.5px;
  }
  .web-band svg { width: 31px; height: 31px; margin-right: 24px; }

  .photo-wave { position: absolute; inset: 0; width: 1200px; height: 1200px; }
</style>
</head>
<body>
<main class="email-card">
  <div class="web-band">
    <svg viewBox="0 0 32 32" aria-hidden="true">
      <circle cx="16" cy="16" r="14" fill="none" stroke="currentColor" stroke-width="2.5"/>
      <ellipse cx="16" cy="16" rx="6" ry="14" fill="none" stroke="currentColor" stroke-width="2"/>
      <path d="M2 16h28M5 9h22M5 23h22" stroke="currentColor" stroke-width="2" fill="none"/>
    </svg>
    <span>www.brightwellrecovery.example</span>
  </div>

  <svg class="photo-wave" viewBox="0 0 1200 1200" aria-hidden="false">
    <defs>
      <linearGradient id="photo-tones" x1="0" y1="0" x2="1" y2="1">
        <stop offset="0" stop-color="#e9e2da"/>
        <stop offset="0.35" stop-color="#c98a6c"/>
        <stop offset="0.6" stop-color="#e6e1dc"/>
        <stop offset="0.8" stop-color="#3a63b8"/>
        <stop offset="1" stop-color="#cfcac4"/>
      </linearGradient>
      <filter id="wave-shadow" x="-10%" y="-10%" width="120%" height="120%">
        <feDropShadow dx="-6" dy="4" stdDeviation="8" flood-color="#000" flood-opacity="0.25"/>
      </filter>
    </defs>
    <path filter="url(#wave-shadow)" fill="#e4e4e6"
      d="M495,0 C610,0 700,110 690,300 C682,440 600,560 598,760 C596,1000 740,1195 900,1198 C1030,1200 1130,1160 1200,1108 L1200,0 Z"/>
    <path filter="url(#wave-shadow)" fill="var(--paper)"
      d="M560,0 C655,10 718,130 704,300 C692,445 614,560 612,760 C610,985 750,1170 900,1174 C1025,1178 1130,1140 1200,1084 L1200,0 Z"/>
    <path role="img" aria-label="Photo: technician in hard hat and blue overalls fitting pipes against a brick wall"
      fill="url(#photo-tones)"
      d="M615,0 C690,20 730,150 716,300 C700,450 628,560 626,760 C624,960 760,1140 900,1150 C1020,1160 1130,1120 1200,1060 L1200,0 Z"/>
  </svg>

  <div class="brand-name">Brightwell Recovery</div>

  <h1 class="headline">Calm<br>Returns</h1>
  <div class="rule rule--headline"></div>

  <p class="intro">Brightwell Recovery, that reflects our commitment to building lasting relationships with our clients and providing top-quality restoration and cleaning services.</p>

  <h2 class="section-title">Our Services</h2>
  <div class="rule rule--services"></div>

  <ul class="service-list">
    <li><svg viewBox="0 0 32 32" aria-hidden="true"><circle cx="16" cy="16" r="13.5" fill="none" stroke="var(--tick)" stroke-width="2"/><path d="M10 16l5 5 9-10" fill="none" stroke="var(--tick)" stroke-width="2.2" stroke-linecap="round" stroke-linejoin="round"/></svg>Water Restoration</li>
    <li><svg viewBox="0 0 32 32" aria-hidden="true"><circle cx="16" cy="16" r="13.5" fill="none" stroke="var(--tick)" stroke-width="2"/><path d="M10 16l5 5 9-10" fill="none" stroke="var(--tick)" stroke-width="2.2" stroke-linecap="round" stroke-linejoin="round"/></svg>Emergency Flood Response</li>
    <li><svg viewBox="0 0 32 32" aria-hidden="true"><circle cx="16" cy="16" r="13.5" fill="none" stroke="var(--tick)" stroke-width="2"/><path d="M10 16l5 5 9-10" fill="none" stroke="var(--tick)" stroke-width="2.2" stroke-linecap="round" stroke-linejoin="round"/></svg>Mold Remediation</li>
    <li><svg viewBox="0 0 32 32" aria-hidden="true"><circle cx="16" cy="16" r="13.5" fill="none" stroke="var(--tick)" stroke-width="2"/><path d="M10 16l5 5 9-10" fill="none" stroke="var(--tick)" stroke-width="2.2" stroke-linecap="round" stroke-linejoin="round"/></svg>Trauma Scene Clean-up</li>
  </ul>

  <a class="cta-button">VIEW ALL</a>
</main>
</body>
</html>
```